High-end residential home builder needs a business card design

We need a new business card design for a small residential construction company based in Boise, Idaho. We specialize in building custom high-end homes and remodels, with a focus on great design and craftsmanship.

We would like to use our current logo, but open to new color suggestions.
Just looking for a clean, sharp, modern design that looks high-end.

Target Market(s)

Upscale clientele

Industry/Entity Type

Contractor

Contact Information for Business Card

Company: Stonefield Custom Builders
Name: Marcus Tilley
Phone number: 208 367 4120
Email: MarcusTilleySCB@mailbox-example.com
Website: Stonefieldcustombuilders-example.com

Font styles to use
Serif
Sans Serif

Requirements
Must have
• Company Logo
Company name
My name
My phone number
My email
Company website
Nice to have
• I have attached a few photos of cards that I really like.

```html
<!DOCTYPE html>
<html lang="en">
<head>
<meta charset="utf-8">
<title>Stonefield Custom Builders — Business Card</title>
<link rel="stylesheet" href="https://fonts.googleapis.com/css2?family=Josefin+Sans:wght@600&family=Noto+Serif:wght@400&display=swap">
<style>
  :root {
    --backdrop: #121212;
    --paper: #ecebea;
    --charcoal: #231f1f;
    --ink: #2b1f1c;
    --gold: #d4922f;
    --light-text: #e9e6e2;
  }
  * { margin: 0; padding: 0; box-sizing: border-box; }
  html, body { width: 1200px; height: 900px; overflow: hidden; background: var(--backdrop); }
  .stage {
    width: 1200px; height: 900px;
    display: flex; flex-direction: column; align-items: center; justify-content: center;
    gap: 64px;
  }
  .card {
    width: 560px; height: 320px;
    background: var(--paper);
    border: 1px solid var(--gold);
    position: relative;
    overflow: hidden;
  }
  .company-mark {
    display: flex; flex-direction: column; align-items: center; gap: 14px;
  }
  .company-mark__square {
    width: 22px; height: 22px; background: var(--gold);
  }
  .company-mark__name {
    font-family: "Josefin Sans", sans-serif;
    font-weight: 600;
    color: var(--ink);
    text-transform: uppercase;
    letter-spacing: 0.22em;
    text-align: center;
    line-height: 1.6;
  }
  .card--front { display: flex; align-items: center; justify-content: center; }
  .card--front .company-mark__name { font-size: 22px; }

  .card--back { display: flex; }
  .card--back .brand-panel {
    width: 42%;
    display: flex; align-items: center; justify-content: center;
  }
  .card--back .company-mark__name { font-size: 14px; }
  .contact-panel {
    flex: 1;
    background: var(--charcoal);
    color: var(--light-text);
    padding: 44px 30px 0 34px;
    font-family: "Noto Serif", serif;
  }
  .contact-panel__name {
    font-size: 33px; font-weight: 400; letter-spacing: 0.01em;
    padding-bottom: 8px;
    border-bottom: 1px solid var(--light-text);
    display: inline-block;
    margin-bottom: 30px;
  }
  .contact-list { list-style: none; display: flex; flex-direction: column; gap: 18px; }
  .contact-list__item { display: flex; align-items: center; gap: 12px; font-size: 12.5px; }
  .contact-list__icon { width: 16px; height: 16px; flex: none; }
</style>
</head>
<body>
<main class="stage">
  <section class="card card--front" aria-label="Business card front">
    <div class="company-mark">
      <span class="company-mark__square"></span>
      <p class="company-mark__name">Stonefield<br>Custom Builders</p>
    </div>
  </section>

  <section class="card card--back" aria-label="Business card back">
    <div class="brand-panel">
      <div class="company-mark">
        <span class="company-mark__square"></span>
        <p class="company-mark__name">Stonefield<br>Custom Builders</p>
      </div>
    </div>
    <div class="contact-panel">
      <h1 class="contact-panel__name">Marcus Tilley</h1>
      <ul class="contact-list">
        <li class="contact-list__item">
          <svg class="contact-list__icon" viewBox="0 0 16 16" fill="none" stroke="currentColor" stroke-width="1.3"><path d="M3 2h3l1 3-2 1a8 8 0 0 0 5 5l1-2 3 1v3a1 1 0 0 1-1 1A12 12 0 0 1 2 3a1 1 0 0 1 1-1z"/></svg>
          <span>208 367 4120</span>
        </li>
        <li class="contact-list__item">
          <svg class="contact-list__icon" viewBox="0 0 16 16" fill="none" stroke="currentColor" stroke-width="1.3"><rect x="1.5" y="3.5" width="13" height="9"/><path d="M1.5 3.5 8 9l6.5-5.5M1.5 12.5 6 8m8.5 4.5L10 8"/></svg>
          <span>MarcusTilleySCB@mailbox-example.com</span>
        </li>
        <li class="contact-list__item">
          <svg class="contact-list__icon" viewBox="0 0 16 16" fill="none" stroke="currentColor" stroke-width="1.2"><circle cx="8" cy="8" r="6.5"/><ellipse cx="8" cy="8" rx="3" ry="6.5"/><path d="M1.5 8h13M2.5 4.8h11M2.5 11.2h11"/></svg>
          <span>Stonefieldcustombuilders-example.com</span>
        </li>
      </ul>
    </div>
  </section>
</main>
</body>
</html>
```